Business Card Design and Logo Needed

I need Business Cards and a Logo for my website and public speaking business which can be found at: www.kelsa-thorn.example

I'm looking for creative and unique ideas. Some business cards I've found online that I like can be found at:
http://gigplatelo.example/general/18-smokin-hot-business-card-designs/

and at

http://www.vortaplume.example/2009/04/50-creative-business-cards-of-50-graphic-designers/

```html
<!DOCTYPE html>
<html lang="en">
<head>
<meta charset="utf-8">
<title>Kelsa Thorn – Business Card</title>
<link rel="stylesheet" href="https://fonts.googleapis.com/css2?family=Charis+SIL&display=swap">
<style>
  :root {
    --page-bg: #ffffff;
    --card-bg: #211c19;
    --accent-green: #86c126;
    --text-light: #e8e6e3;
    --text-white: #ffffff;
  }
  html, body {
    margin: 0;
    padding: 0;
    width: 1200px;
    height: 900px;
    overflow: hidden;
    background: var(--page-bg);
  }
  .canvas {
    position: relative;
    width: 1200px;
    height: 900px;
    font-family: "Charis SIL", serif;
  }
  .business-card {
    position: absolute;
    left: 75px;
    top: 148px;
    width: 1052px;
    height: 602px;
    border-radius: 33px;
    background: var(--card-bg);
  }
  .tagline-band {
    position: absolute;
    left: 97px;
    top: 367px;
    width: 811px;
    height: 163px;
  }
  .website {
    position: absolute;
    left: 99px;
    top: 336px;
    margin: 0;
    font-size: 30px;
    line-height: 30px;
    color: var(--text-light);
  }
  .tagline {
    position: absolute;
    left: 112px;
    top: 422px;
    margin: 0;
    font-size: 46px;
    line-height: 46px;
    font-weight: 400;
    color: var(--text-white);
  }
  .contact-details {
    position: absolute;
    left: 98px;
    top: 532px;
    margin: 0;
    font-style: normal;
    font-size: 30px;
    line-height: 45px;
    color: var(--text-light);
  }
  .contact-details span { display: block; }
</style>
</head>
<body>
<main class="canvas">
  <section class="business-card" aria-label="Business card"></section>

  <svg class="tagline-band" viewBox="0 0 811 163" aria-hidden="true">
    <path d="M0 0 H683 C760 0 811 36 811 81.5 C811 127 760 163 683 163 H0 Z" fill="var(--accent-green)"/>
  </svg>

  <p class="website">www.kelsa-thorn.example</p>
  <h1 class="tagline">speaker-philanthropist-author</h1>

  <address class="contact-details">
    <span class="email">info@kelsa-thorn.example</span>
    <span class="phone">+23 - 48201937</span>
    <span class="city">city name</span>
    <span class="zip">zip code</span>
  </address>
</main>
</body>
</html>
```